Corvella Web Design Project

I am attaching my logo so I need to see applied to the website developed by you guys!!
Tbahks!!
Marcello
This is the DNA of the company
Flat and dynamic organization - Informal and respectful social approac
Innovative - Always striving for the best solution
Reliability and Quality - The value of our name
Flexibility - Ability to handle new requirements and unforeseen events
Simplicity - Technology must serve – NOT rule!
Cooperative Relations - The synergy that makes 1+1=3
We still don´t have our logo as we have another open project on artbazaar
Our company won´t be selling this equipment but providing welding services for shipyard industry, as you can see on the website below.
www.velmorix.com
Updates
Project Deadline Extended
Reason: Hi webdesigners,
I will be deciding my logo by this weekend as soon as I have decided I will post my logo to see it applied to your design!!!
Thanks
Marcello
I just Sent my logo for your attention!!!!
Industry/Entity Type
Welding
Look and feel
Each slider illustrates characteristics of the customer's brand and the style your logo design should communicate.

```html
<!DOCTYPE html>
<html lang="en">
<head>
<meta charset="utf-8">
<title>Velmorix – Welding Automation</title>
<link href="https://fonts.googleapis.com/css2?family=PT+Sans+Narrow:wght@400;700&display=swap" rel="stylesheet">
<style>
:root{
  --bg:#1d1d1d;
  --bg-dark:#121212;
  --header:#161616;
  --footer:#151515;
  --yellow:#f3b21c;
  --blue:#1d9ad8;
  --blue-deep:#127bb5;
  --text:#ffffff;
  --muted:#cfcfcf;
}
*{box-sizing:border-box;margin:0;padding:0}
html,body{width:964px;height:1200px;overflow:hidden}
body{
  position:relative;
  background:radial-gradient(ellipse at 60% 45%,#2a2a2a 0%,var(--bg) 55%,var(--bg-dark) 100%);
  font-family:"PT Sans Narrow",sans-serif;color:var(--text);
}
.abs{position:absolute}
.site-header{left:0;top:26px;width:964px;height:107px;background:var(--header)}
.phone-box{left:658px;top:26px;width:174px;height:39px;border:1px solid #333;border-top:none;border-radius:0 0 6px 6px;background:#111;display:flex;align-items:center;gap:9px;padding-left:24px;color:var(--blue);font-size:16px}
.brand{left:126px;top:74px;display:flex;align-items:center;gap:8px}
.brand-name{font-size:34px;font-weight:400;line-height:1;color:var(--text)}
.brand-mark{width:12px;height:12px;border-radius:50%;background:var(--blue)}
.main-nav{right:133px;top:97px;display:flex;gap:18px;font-size:14px}
.main-nav a{color:var(--text);text-decoration:none}
.main-nav a.active{color:var(--blue)}
.hero{left:126px;top:158px;width:508px;height:317px;background:radial-gradient(circle at 38% 62%,#e29a3a 0%,#8a5a2a 25%,#4a3a30 55%,#2c2624 100%)}
.hero-caption{left:126px;top:434px;width:508px;height:41px;background:rgba(30,30,30,.72);display:flex;align-items:center;justify-content:space-between;padding:0 20px 0 24px;font-size:21px}
.dots{display:flex;gap:4px}
.dots span{width:5px;height:5px;border-radius:50%;background:#fff}
.dots span:first-child{background:var(--blue)}
.news{left:634px;top:158px;width:199px;height:317px;background:linear-gradient(160deg,var(--blue) 0%,var(--blue-deep) 100%);padding:20px 15px}
.news h2{font-size:21px;font-weight:400;color:#111;margin-bottom:8px}
.news h2 span{color:#fff}
.news p{font-size:8.6px;font-style:italic;line-height:12.8px;color:#fff}
.news time{display:block;font-size:8.5px;color:#111;margin:8px 0 13px}
.news hr{border:none;border-top:1px solid rgba(0,0,0,.35);margin-bottom:13px}
.card{top:500px;width:222px}
.card-photo{height:154px}
.card h3{font-size:21px;color:var(--yellow);font-weight:700;margin:14px 0 4px}
.card p{font-size:9.5px;line-height:13px;color:#e6e6e6}
.btn-arrow{display:inline-flex;align-items:center;margin-top:17px;height:22px}
.btn-arrow span{background:var(--yellow);color:#111;font-size:10px;padding:0 10px;height:22px;line-height:22px}
.btn-arrow i{width:0;height:0;border-top:11px solid transparent;border-bottom:11px solid transparent;border-left:13px solid var(--yellow)}
.welcome{left:0;top:818px;width:964px;text-align:center}
.welcome h2{font-size:21px;font-weight:700}
.welcome .rule{position:absolute;top:13px;width:154px;border-top:1px solid #000}
.welcome .sub{font-size:9.5px;color:var(--yellow);margin-top:2px}
.welcome .intro{font-size:9.5px;line-height:13px;margin-top:19px}
.points{left:340px;top:918px;display:grid;grid-template-columns:151px 180px;row-gap:9px;font-size:9.5px}
.points li{list-style:none;display:flex;align-items:center;gap:7px;height:17px;white-space:nowrap}
.points a{color:var(--yellow);padding-left:26px}
.site-footer{left:0;top:1034px;width:964px;height:166px;background:var(--footer)}
.f-col{top:1060px}
.f-col h4{font-size:17px;font-weight:400;color:var(--yellow);margin-bottom:5px}
.f-col p{font-size:9.3px;line-height:12.8px;color:var(--muted)}
.f-col a{color:var(--yellow);font-size:9.3px;font-style:italic}
.social{display:flex;gap:5px;margin-top:11px}
.social span{width:16px;height:16px;border-radius:50%;background:var(--yellow)}
.email{width:177px;height:26px;background:#0b0b0b;border:1px solid #333;color:#888;font-size:9.3px;padding:0 10px;line-height:24px;margin-top:8px}
.submit{width:64px;height:26px;background:var(--yellow);color:#111;font-size:12px;text-align:center;line-height:26px;margin-top:6px}
</style>
</head>
<body>
<header class="abs site-header"></header>
<div class="abs phone-box">
  <svg width="18" height="18" viewBox="0 0 18 18"><circle cx="9" cy="9" r="8" fill="none" stroke="#9a9a9a" stroke-width="1.3"/><path d="M6 5.2l1.6-.4 1 2.2-1 .8a5 5 0 0 0 2.5 2.5l.8-1 2.2 1-.4 1.6c-3.8.4-7.1-2.9-6.7-6.7z" fill="#9a9a9a"/></svg>
  +45 7132 5580
</div>
<div class="abs brand">
  <span class="brand-mark"></span><span class="brand-name">Velmorix</span>
</div>
<nav class="abs main-nav">
  <a class="active" href="#">Home</a><a href="#">About Us</a><a href="#">Competence</a><a href="#">Case Story</a><a href="#">Products</a><a href="#">Videos</a><a href="#">Downloads</a>
</nav>

<div class="abs hero" role="img" aria-label="Welder in goggles working with a cutting torch, sparks flying"></div>
<div class="abs hero-caption"><span>Velmorix Denmark</span><div class="dots"><span></span><span></span><span></span><span></span></div></div>

<aside class="abs news">
  <h2>Latest <span>News</span></h2>
  <p>Velmorix ApS is happy to announce new strong people in the management, new constellation in the ownership and an extremely strong board of directors. See more under "About us" &amp; "NEWS".</p>
  <time>09 Oct, 2014</time>
  <hr>
  <p>Lorem ipsum dolor sit amet, consectetur adipisicing elit, sed do eiusmod tempor incididunt ut labore et dolore magna aliqua. Lorem ipsum dolor sit amet, consectetur adipisicing elit, sed do eiusmod tempor incididunt ut labore et dolore magna aliqua. Lorem ipsum dolor sit amet, consectetur adipisicing elit, sed do eiusmod tempor incididunt ut labore et dolore magna aliqua.</p>
  <time>16 Oct, 2014</time>
</aside>

<section class="abs card" style="left:126px">
  <div class="card-photo" role="img" aria-label="Worker in hard hat drilling on a steel structure" style="background:linear-gradient(135deg,#8fb3a8,#3b4a6a 55%,#c9a530)"></div>
  <h3>Case Story</h3>
  <p>Lorem ipsum dolor sit amet, consectetur adipisicing elit, sed do eiusmod tempor incididunt ut labore et dolore magna aliqua.</p>
  <div class="btn-arrow"><span>More...</span><i></i></div>
</section>
<section class="abs card" style="left:369px">
  <div class="card-photo" role="img" aria-label="Ship hull in a dry dock with a worker below" style="background:linear-gradient(180deg,#c8ccd0,#55585c 45%,#6b5a4c)"></div>
  <h3>Competence</h3>
  <p>Lorem ipsum dolor sit amet, consectetur adipisicing elit, sed do eiusmod tempor incididunt ut labore et dolore magna aliqua.</p>
  <div class="btn-arrow"><span>More...</span><i></i></div>
</section>
<section class="abs card" style="left:612px">
  <div class="card-photo" role="img" aria-label="Worker grinding steel with sparks" style="background:linear-gradient(135deg,#d99a2a,#6a6a6a 50%,#9a9ea2)"></div>
  <h3>Videos</h3>
  <p>Lorem ipsum dolor sit amet, consectetur adipisicing elit, sed do eiusmod tempor incididunt ut labore et dolore magna aliqua.</p>
  <div class="btn-arrow"><span>See it...</span><i></i></div>
</section>

<section class="abs welcome">
  <span class="rule" style="left:240px"></span><span class="rule" style="left:574px"></span>
  <h2>Welcome to our site</h2>
  <p class="sub">Welding Automation - Velmorix featuring ASWT</p>
  <p class="intro">With the innovation; ASWT (Adaptive Seam Welding Technology) Velmorix from Denmark has set new standards for future welding automation technology world wide.<br>Key points are:</p>
</section>
<ul class="abs points">
  <li><svg width="17" height="17" viewBox="0 0 17 17"><circle cx="8.5" cy="8.5" r="7.5" fill="none" stroke="#f3b21c" stroke-width="1.5"/><path d="M5 8.7l2.4 2.3 4.6-4.8" fill="none" stroke="#f3b21c" stroke-width="1.6"/></svg>Self programming robot intelligens</li>
  <li><svg width="17" height="17" viewBox="0 0 17 17"><circle cx="8.5" cy="8.5" r="7.5" fill="none" stroke="#f3b21c" stroke-width="1.5"/><path d="M5 8.7l2.4 2.3 4.6-4.8" fill="none" stroke="#f3b21c" stroke-width="1.6"/></svg>Very simple and intuitive operation</li>
  <li><svg width="17" height="17" viewBox="0 0 17 17"><circle cx="8.5" cy="8.5" r="7.5" fill="none" stroke="#f3b21c" stroke-width="1.5"/><path d="M5 8.7l2.4 2.3 4.6-4.8" fill="none" stroke="#f3b21c" stroke-width="1.6"/></svg>No engineering back-up required</li>
  <li><svg width="17" height="17" viewBox="0 0 17 17"><circle cx="8.5" cy="8.5" r="7.5" fill="none" stroke="#f3b21c" stroke-width="1.5"/><path d="M5 8.7l2.4 2.3 4.6-4.8" fill="none" stroke="#f3b21c" stroke-width="1.6"/></svg>Ease of installation and implementation</li>
  <li><svg width="17" height="17" viewBox="0 0 17 17"><circle cx="8.5" cy="8.5" r="7.5" fill="none" stroke="#f3b21c" stroke-width="1.5"/><path d="M5 8.7l2.4 2.3 4.6-4.8" fill="none" stroke="#f3b21c" stroke-width="1.6"/></svg>No CAD or drawing interface needed . . .</li>
  <li><a href="#">and Many more &gt;</a></li>
</ul>

<footer class="abs site-footer"></footer>
<div class="abs f-col" style="left:127px;width:210px">
  <h4>About Us</h4>
  <p>Lorem ipsum dolor sit amet, consectetur adipisicing elit, sed do eiusmod tempor incididunt ut labore et dolore magna aliqua. Lorem ipsum dolor sit amet, consectetur adipisicing elit, sed do eiusmod tempor incididunt ut labore et dolore.</p>
  <p style="margin-top:9px"><a href="#">Read more...</a></p>
</div>
<div class="abs f-col" style="left:382px;width:210px">
  <h4>Contact Us</h4>
  <p>Velmorix<br>Brovænget 12, 5210 Vestby N, Denmark<br>Phone : +45 7132 5580 / Email : info@velmorix.com</p>
  <div class="social"><span></span><span></span><span></span></div>
</div>
<div class="abs f-col" style="left:612px;width:200px">
  <h4>Subscribe Us</h4>
  <div class="email">Your Email id</div>
  <div class="submit">Submit</div>
</div>
</body>
</html>
```